Business Card for Wellness Clinic

We need a business card for our new logo. I want it to match the feel of the logo

Target Market(s)

Young professional families looking for holistic health care

Industry/Entity Type

Health And Wellness

Contact Information for Business Card

Our business Name: Brackenfield Health & wellness Centre, our phone #, email address...see attached old business card

Font styles to use
Sans Serif

Colors
33b8a4
cee9f5

Requirements
Must have
• my logo and business name
• Font is "Helvetica Neue LT Std 45 Light" and
• Only for "&" using font "Trajan pro bold"
• Use colors in the logo

```html
<!DOCTYPE html>
<html lang="en">
<head>
<meta charset="utf-8">
<title>Brackenfield Health &amp; wellness Centre – Business Cards</title>
<link rel="stylesheet" href="https://fonts.googleapis.com/css2?family=Roboto:wght@300;400&family=Quattrocento:wght@400;700&display=swap">
<style>
  :root {
    --teal: #33b8a4;
    --backdrop: #a9a6a6;
    --card: #f7f7f7;
    --ink: #5a5a5a;
    --ink-soft: #6e6e6e;
    --rule: #8a8a8a;
    --divider: #dcdcdc;
  }
  * { margin: 0; padding: 0; box-sizing: border-box; }
  html, body { width: 1200px; height: 1200px; overflow: hidden; }
  body { background: var(--backdrop); position: relative; font-family: "Roboto", Arial, sans-serif; }

  .card { position: absolute; width: 712px; height: 418px; background: var(--card); overflow: hidden; }
  .card--appointment { left: 238px; top: 119px; }
  .card--contact { left: 231px; top: 644px; height: 417px; }

  .brand-mark { position: absolute; background: var(--teal); border-radius: 6px; }
  .brand-name {
    position: absolute; font-family: "Roboto", Arial, sans-serif; font-weight: 300;
    color: var(--ink-soft); letter-spacing: 4px; text-transform: uppercase; line-height: 1.35;
  }

  /* appointment side */
  .card--appointment .brand-mark { left: 120px; top: 48px; width: 70px; height: 70px; }
  .card--appointment .brand-name { left: 210px; top: 60px; font-size: 21px; }

  .form-row { position: absolute; left: 40px; right: 40px; display: flex; align-items: flex-end; font-size: 20px; color: var(--ink); }
  .form-row--date { top: 194px; }
  .form-row--for { top: 262px; }
  .form-line { flex: 1; border-bottom: 1.5px solid var(--rule); margin: 0 6px 4px 6px; }
  .form-line--date { flex: 0 0 358px; }
  .form-line--time { flex: 1; margin-right: 0; }
  .form-row--for .form-line { margin-right: 0; }

  .notice { position: absolute; left: 0; right: 0; top: 324px; text-align: center; font-size: 18px; line-height: 24px; color: var(--ink); }

  /* contact side */
  .card--contact .brand-mark { left: 137px; top: 90px; width: 76px; height: 76px; }
  .card--contact .brand-name { left: 0; width: 345px; top: 216px; text-align: center; font-size: 19px; }
  .divider { position: absolute; left: 345px; top: 68px; width: 1px; height: 218px; background: var(--divider); }

  .person { position: absolute; left: 380px; top: 96px; font-family: "Quattrocento", Georgia, serif; }
  .person__name { font-size: 27px; font-weight: 700; color: var(--teal); }
  .person__title { font-size: 19px; color: var(--ink-soft); margin-top: 6px; }

  .contact-list { position: absolute; left: 380px; top: 176px; list-style: none; font-family: "Quattrocento", Georgia, serif; font-size: 19px; color: var(--ink-soft); }
  .contact-list li { display: flex; align-items: center; height: 26px; }
  .contact-list svg { width: 18px; height: 18px; margin-right: 17px; fill: var(--teal); }

  .address-band { position: absolute; left: 0; right: 0; bottom: 0; height: 64px; background: var(--teal);
    display: flex; align-items: center; justify-content: center;
    font-family: "Quattrocento", Georgia, serif; font-size: 19px; color: #fff; }
</style>
</head>
<body>

<section class="card card--appointment" aria-label="Appointment card">
  <div class="brand-mark"></div>
  <div class="brand-name">Brackenfield Health<br>&amp; Wellness Centre</div>

  <div class="form-row form-row--date">
    <span>Date:</span><span class="form-line form-line--date"></span>
    <span>Time :</span><span class="form-line form-line--time"></span>
  </div>
  <div class="form-row form-row--for">
    <span>For:</span><span class="form-line"></span>
  </div>

  <p class="notice">If you are unable to keep your appointment, please provide<br>at least 2 business days notice or full visit fees will apply.</p>
</section>

<section class="card card--contact" aria-label="Business card">
  <div class="brand-mark"></div>
  <div class="brand-name">Brackenfield Health<br>&amp; Wellness Centre</div>
  <div class="divider"></div>

  <div class="person">
    <div class="person__name">Dr. Maren Holt, N.D.</div>
    <div class="person__title">Naturopathic Doctor</div>
  </div>

  <ul class="contact-list">
    <li>
      <svg viewBox="0 0 24 24" aria-hidden="true"><path d="M3 8c0-3 4-4 9-4s9 1 9 4v2h-5V8H8v2H3V8zm3 4h12l2 8H4l2-8zm6 1.5a3 3 0 100 6 3 3 0 000-6z"/></svg>
      613-555-0147
    </li>
    <li>
      <svg viewBox="0 0 24 24" aria-hidden="true"><path d="M2 5h20v14H2V5zm2 2v.5l8 5.5 8-5.5V7H4zm0 3v7h16v-7l-8 5.5L4 10z"/></svg>
      mholt@capitalnaturopathic.ca
    </li>
    <li>
      <svg viewBox="0 0 24 24" aria-hidden="true"><path d="M12 2a10 10 0 100 20 10 10 0 000-20zm-1 2.1V8H7.6A8 8 0 0111 4.1zm2 0A8 8 0 0116.4 8H13V4.1zM6.7 10H11v4H6.7a8 8 0 010-4zm6.3 0h4.3a8 8 0 010 4H13v-4zm-5.4 6H11v3.9A8 8 0 017.6 16zm5.4 0h3.4a8 8 0 01-3.4 3.9V16z"/></svg>
      www.capitalnaturopathic.ca
    </li>
  </ul>

  <div class="address-band">48 Larchmont Ave, Suite 305 Ottawa, ON K1R 2B6</div>
</section>

</body>
</html>
```